Video Company Business Card Design

We are looking for a new design for business cards that will complement our new logo and new website design.

Target Market(s)

professionals who need video work done

Industry/Entity Type

Business

Requirements
Must have
• Logo
compliment website look seen here...http://k7pixelworks.example/brightlane/

info for card:
Dana Whitlow
Producer/ Cinematographer

532 Pellingham NE
Cedar Hollow, WA 98012
(inside The RAVN Hall)
(616) 555-0142
Dana@brightlanemedia.example
www.brightlanemedia.example

```html
<!DOCTYPE html>
<html lang="en">
<head>
<meta charset="utf-8">
<title>Brightlane Media — Business Card</title>
<link href="https://fonts.googleapis.com/css2?family=Oswald:wght@600;700&family=Roboto+Condensed:wght@400;700&display=swap" rel="stylesheet">
<style>
  :root {
    --page: #f4f4f4;
    --slate: #6b6c6f;
    --green: #1f9a3e;
    --green-deep: #0e7a34;
    --ink: #1d1d1d;
    --text: #333333;
    --icon: #8a8a8a;
    --paper: #f7f7f7;
    --mist-light: #eceeed;
    --mist-dark: #b9bcbc;
  }
  * { box-sizing: border-box; margin: 0; padding: 0; }
  html, body { width: 1200px; height: 900px; overflow: hidden; background: var(--page); }
  body { position: relative; font-family: "Roboto Condensed", Arial, sans-serif; }

  .card {
    position: absolute;
    top: 290px;
    width: 555px;
    height: 320px;
    overflow: hidden;
    box-shadow: 2px 3px 8px rgba(0,0,0,.28);
  }
  .card--front { left: 30px; background: var(--slate); }
  .card--back { left: 615px; background: var(--paper); }

  /* Front */
  .front__visual {
    position: absolute; left: 314px; top: 0; width: 241px; height: 320px;
    background: linear-gradient(135deg, var(--mist-light) 0%, #c9cccb 45%, #8fc79d 62%, var(--mist-dark) 100%);
  }
  .front__bar {
    position: absolute; right: 0; width: 205px; height: 13px; background: var(--green-deep);
  }
  .front__bar--top { top: 0; }
  .front__bar--bottom { bottom: 0; }
  .front__brand {
    position: absolute; left: 36px; top: 142px;
    display: flex; align-items: center; gap: 8px;
  }

  .brand__name {
    font-family: "Roboto Condensed", Arial, sans-serif;
    font-weight: 700;
    font-size: 22px;
    letter-spacing: .5px;
    color: var(--green);
    text-transform: uppercase;
    white-space: nowrap;
  }
  .brand__mark { width: 16px; height: 16px; background: var(--green); }

  /* Back */
  .back__visual {
    position: absolute; right: 0; top: 0; width: 400px; height: 320px;
    background: radial-gradient(ellipse at 55% 40%, #e3e4e4 0%, #eeeeee 45%, var(--paper) 75%);
  }
  .back__content { position: absolute; left: 24px; top: 20px; width: 260px; }
  .person__name {
    font-family: "Oswald", "Arial Narrow", sans-serif;
    font-weight: 700; font-size: 33px; line-height: 1; letter-spacing: 1px;
    color: var(--ink); text-transform: uppercase; white-space: nowrap;
  }
  .person__name .accent { color: var(--green); }
  .person__role {
    margin-top: 4px; font-size: 13px; color: var(--green); text-transform: uppercase; letter-spacing: .3px;
  }
  .rule { height: 1.5px; background: var(--green); width: 215px; }
  .rule--top { margin-top: 18px; }
  .rule--bottom { margin-top: 10px; }
  .contact { list-style: none; margin-top: 10px; }
  .contact__item {
    display: flex; align-items: center; gap: 14px; height: 34px;
    font-size: 12.5px; color: var(--text); white-space: nowrap;
  }
  .contact__icon { width: 24px; height: 20px; flex: none; }
  .address { margin-top: 6px; font-size: 12.5px; line-height: 1.35; color: var(--text); white-space: nowrap; }
  .back__brand {
    position: absolute; right: 30px; bottom: 26px;
    display: flex; align-items: center; gap: 8px;
  }
</style>
</head>
<body>

<section class="card card--front" aria-label="Card front">
  <div class="front__visual" role="img" aria-label="Film strip curving into a countdown circle on soft grey and green"></div>
  <div class="front__bar front__bar--top"></div>
  <div class="front__bar front__bar--bottom"></div>
  <div class="front__brand">
    <span class="brand__name">Brightlane Media</span>
    <span class="brand__mark"></span>
  </div>
</section>

<section class="card card--back" aria-label="Card back">
  <div class="back__visual" role="img" aria-label="Faint film reel and film strip in light grey"></div>
  <div class="back__content">
    <h1 class="person__name">Dana <span class="accent">Whitlow</span></h1>
    <p class="person__role">Producer/Cinematographer</p>
    <div class="rule rule--top"></div>
    <ul class="contact">
      <li class="contact__item">
        <svg class="contact__icon" viewBox="0 0 24 20" aria-hidden="true">
          <path d="M2 7 Q12 0 22 7 L19 9 L16 7 L8 7 L5 9 Z" fill="var(--icon)"/>
          <rect x="5" y="9" width="14" height="9" rx="2" fill="var(--icon)"/>
          <circle cx="12" cy="13.5" r="2.5" fill="var(--paper)"/>
        </svg>
        <span>555/555 0142</span>
      </li>
      <li class="contact__item">
        <svg class="contact__icon" viewBox="0 0 24 20" aria-hidden="true">
          <rect x="2" y="3" width="20" height="14" fill="none" stroke="var(--icon)" stroke-width="1.6"/>
          <path d="M2 3 L12 11 L22 3 M2 17 L9 9 M22 17 L15 9" fill="none" stroke="var(--icon)" stroke-width="1.4"/>
        </svg>
        <span>Dana@brightlanemedia.example</span>
      </li>
      <li class="contact__item">
        <svg class="contact__icon" viewBox="0 0 24 20" aria-hidden="true">
          <path d="M10 1 L10 12 L7 10 L6 12 L11 19 L19 19 L19 10 L13 8 L13 1 Z" fill="var(--icon)"/>
        </svg>
        <span>www.brightlanemedia.example</span>
      </li>
    </ul>
    <div class="rule rule--bottom"></div>
    <p class="address">532 Pellingham NE Cedar Hollow, WA 98012<br>(inside The RAVN Hall)</p>
  </div>
  <div class="back__brand">
    <span class="brand__name">Brightlane Media</span>
    <span class="brand__mark"></span>
  </div>
</section>

</body>
</html>
```